Verdel Harvest Co - Business Card Design Project

We need business cards for our business. We grow roots and fruits in Central and South America, we import and distribute in FL, USA. We do fresh and frozen products.

Target Market(s)

Small and big supermarkets, wholesalers, traders, distributors, etc

Industry/Entity Type

Business

```html
<!DOCTYPE html>
<html lang="en">
<head>
<meta charset="utf-8">
<title>Verdel Harvest Co – Business Card</title>
<link href="https://fonts.googleapis.com/css2?family=Lato:wght@300;400;700&display=swap" rel="stylesheet">
<style>
  :root {
    --page-bg: #ecebe6;
    --card-bg: #fbfbf9;
    --leaf-green: #5f7d3a;
    --band-green: #587436;
    --harvest-orange: #f0921e;
    --muted-text: #8c9478;
    --rule: #a9b195;
  }
  * { margin: 0; padding: 0; box-sizing: border-box; }
  html, body {
    width: 1200px;
    height: 818px;
    overflow: hidden;
    background: var(--page-bg);
    font-family: "Lato", sans-serif;
  }
  .card {
    position: absolute;
    left: 150px;
    top: 152px;
    width: 900px;
    height: 514px;
    background: var(--card-bg);
    box-shadow: 0 10px 30px rgba(0,0,0,0.12);
    overflow: hidden;
  }
  .card-content {
    position: absolute;
    left: 0; right: 0; top: 52px;
    text-align: center;
  }
  .brand-name {
    display: inline-flex;
    align-items: center;
    gap: 16px;
    font-size: 62px;
    font-weight: 400;
    letter-spacing: 1px;
    color: var(--leaf-green);
  }
  .brand-dot {
    width: 26px; height: 26px;
    border-radius: 50%;
    background: var(--leaf-green);
  }
  .tagline {
    margin-top: 18px;
    font-size: 20px;
    font-weight: 400;
    color: var(--muted-text);
  }
  .person {
    margin: 40px auto 0;
    display: flex;
    align-items: center;
    justify-content: center;
    gap: 22px;
  }
  .person-rule {
    width: 110px;
    height: 1px;
    background: var(--rule);
  }
  .person-name {
    font-size: 30px;
    font-weight: 700;
    color: var(--harvest-orange);
    line-height: 1;
  }
  .person-title {
    margin-top: 6px;
    font-size: 16px;
    color: var(--muted-text);
  }
  .about {
    margin-top: 34px;
    font-size: 25px;
    line-height: 1.3;
    color: var(--leaf-green);
  }
  .card-band {
    position: absolute;
    left: 0; right: 0; bottom: 0;
    height: 66px;
    background: var(--band-green);
  }
  .card-band::before {
    content: "";
    position: absolute;
    left: 0; right: 0; top: 8px;
    height: 2px;
    background: var(--card-bg);
  }
  .card-band::after {
    content: "";
    position: absolute;
    left: 0; right: 0; top: -12px;
    height: 2px;
    background: var(--band-green);
  }
</style>
</head>
<body>
  <section class="card" aria-label="Business card front">
    <div class="card-content">
      <div class="brand-name"><span class="brand-dot"></span>Verdel Harvest Co</div>
      <p class="tagline">We grow roots and fruits in Central and South America</p>
      <div class="person">
        <span class="person-rule"></span>
        <div>
          <div class="person-name">MARCUS ELLERY</div>
          <div class="person-title">Managing Director</div>
        </div>
        <span class="person-rule"></span>
      </div>
      <p class="about">We do fresh and frozen products<br>we import and distribute in FL, USA</p>
    </div>
    <div class="card-band"></div>
  </section>
</body>
</html>
```